HALVERWOOD MARKSMAN SPORTS, A modern indoor gun range comfortable for anyone to visit.

Please note the attached "Operating Plan", and "Letter of Introduction" for more details on our operation.

What we are looking for is the overall feel and look of the website. A lot of the details in how many links, what links, etc we will have built later. It's more important we get the right color scheme, flow, feel, etc.

This is an indoor gun range in Colorado. We are looking to be the skyline putt of the gun industry. We want a website that is simple, but stylish. Our range is forward thinking and modern. Please see our logo attached.

Our indoor range will also have a small cafe that will sell coffee, mixed soda drinks, and made from scratch cinnamon rolls.

Our look will be lighter colors. We want to avoid anything that would seem aggressive. Simple is the key here. We love simple clean designs. Pixel harbor has a good look and feel to it. Something with the same feel would be great. Our logo is red and black; however, we don't want the website to be dominated by those colors. Blue is also a great color.

We need a landing page that can shrink to different sizes of screens.
No mobile format.
Contact page with email submission
Menu will only have a couple links. We are open to different formats. Skyline putts format is also a good design.

Possible links will include: Home, Membership, About Us, Contact Us, Classes, Cafe

Target Market(s)

Primary target is male 35-55 years old with some college or more.

Number of Pages Required

3 page

Font styles to use
Sans Serif

Colors

Designer to choose colors to be used in the design.

Requirements
Must have
• Page 1 Landing first page
• Page 2 Blog posts to give updates on building progress
• Page 3 About us (hours of operation, etc)

```html
<!DOCTYPE html>
<html lang="en">
<head>
<meta charset="utf-8">
<title>Halverwood Marksman Sports</title>
<link href="https://fonts.googleapis.com/css2?family=Noto+Serif:wght@400;700&display=swap" rel="stylesheet">
<style>
:root{
  --blue:#2f73bb;
  --blue-link:#3a7cc4;
  --ink:#222;
  --body:#555;
  --dark:#1f2227;
  --footer:#161616;
  --white:#fff;
  --line:#cfcfcf;
}
*{box-sizing:border-box;margin:0;padding:0}
html,body{width:1200px;height:3662px;overflow:hidden}
body{font-family:"Noto Serif",serif;color:var(--ink);position:relative;background:#fff;letter-spacing:.06em}
.abs{position:absolute}
.flag{display:inline-block;width:50px;height:24px;background:var(--blue);clip-path:polygon(8% 0,100% 0,92% 100%,0 100%);vertical-align:middle;margin-right:18px}
h2{font-size:27px;font-weight:700;letter-spacing:.12em}
/* hero */
.hero{left:0;top:0;width:1200px;height:520px;background:linear-gradient(90deg,#2b3140 0%,#5c5a55 35%,#8a7357 60%,#6e5a44 100%)}
.topbar{left:0;top:0;width:1200px;height:125px;background:rgba(20,22,28,.75)}
.brand{left:36px;top:36px;display:flex;align-items:center;gap:14px;color:#fff;font-size:17px;font-weight:700;line-height:1.15;white-space:nowrap}
.brand i{width:34px;height:34px;border-radius:50%;border:3px solid #fff;flex:none}
.contact{right:34px;top:24px;color:#fff;font-size:15px}
.contact span{margin-left:30px}
.nav{right:34px;top:78px;display:flex;gap:32px;font-size:15px;color:#fff}
.nav .on{color:#3b9be0;font-weight:700}
.hero-box{left:36px;top:210px;width:533px;height:188px;background:rgba(20,22,28,.82);padding:16px 52px;color:#fff}
.hero-box h1{font-size:24px;line-height:1.55;letter-spacing:.1em}
.hero-box p{font-size:12.5px;line-height:1.7;margin-top:12px;letter-spacing:.04em}
.btn-read{left:36px;top:444px;width:157px;height:39px;background:var(--blue);color:#fff;font-size:14px;font-weight:700;display:flex;align-items:center;justify-content:center;clip-path:polygon(6% 0,100% 0,100% 100%,0 100%)}
.btn-contact{left:193px;top:444px;width:155px;height:39px;border:1px solid var(--blue);border-left:0;color:#fff;font-size:14px;font-weight:700;display:flex;align-items:center;justify-content:center}
/* who */
.who-title{left:36px;top:585px}
.who-text{left:36px;top:678px;width:615px;font-size:13.5px;line-height:1.65;color:var(--body)}
.who-text p{margin-bottom:22px}
.link{color:var(--blue-link);font-weight:700;font-size:15px}
.tiles{left:803px;top:677px;width:363px}
.tile{position:relative;height:97px;display:flex;align-items:center;padding-left:55px;justify-content:space-between;padding-right:70px}
.tile .edge{position:absolute;left:0;top:0;width:363px;height:97px}
.tile div,.tile .ico{position:relative}
.tile b{display:block;font-size:17px}
.tile small{color:var(--blue-link);font-size:13px}
/* dark section */
.range{left:0;top:1042px;width:1200px;height:735px;background:radial-gradient(ellipse at 55% 40%,#3d434b,#262a31 70%)}
.range-title{left:0;top:1106px;width:1200px;text-align:center;color:#fff}
.range-text{left:130px;top:1204px;width:940px;text-align:center;color:#fff;font-size:17.5px;line-height:1.55}
.card{background:#fff}
.card-head{height:50px;background:var(--blue);color:#fff;font-size:18px;font-weight:700;display:flex;align-items:center;padding-left:20px;gap:14px}
.card-head i{width:22px;height:22px;border:2px solid #fff;border-radius:50%}
.hours{left:88px;top:1362px;width:344px;height:348px}
.hours .in{padding:38px 25px;font-size:15px;line-height:1.85}
.red{color:#d0232a;font-weight:700}
.blue-b{color:var(--blue-link);font-weight:700;margin-top:22px;text-align:justify}
.member{left:499px;top:1362px;width:614px;height:348px}
.member .in{padding:36px 44px}
.member h3{font-size:18px;margin-bottom:22px}
.member p{font-size:15px;line-height:2.2;color:var(--body)}
.member .more{text-align:right;color:var(--blue-link);font-weight:700;font-size:17px;margin-top:4px}
/* cafe */
.cafe-title{left:0;top:1843px;width:1200px;text-align:center}
.cafe-desc{left:250px;top:1902px;width:700px;text-align:center;font-size:13px;color:var(--body);line-height:1.7}
.food{top:1999px;width:277px}
.food .img{height:319px}
.food .cap{display:flex;justify-content:space-between;margin-top:22px;font-size:15px}
.food .cap span:last-child{color:var(--blue-link)}
/* testimonial */
.testi{left:0;top:2424px;width:1200px;height:337px;background:linear-gradient(90deg,#14171c,#2b2520 45%,#1a1d22 100%)}
.testi-title{left:0;top:2477px;width:1200px;text-align:center;color:#fff}
.quote{left:0;top:2568px;width:1200px;text-align:center;color:#fff;font-size:80px;line-height:1;font-weight:700}
.testi-text{left:200px;top:2636px;width:800px;text-align:center;color:#fff;font-size:14px;line-height:1.6}
.arrow{top:2616px;width:52px;height:36px;background:var(--blue)}
/* events */
.ev-title{left:0;top:2826px;width:1200px;text-align:center}
.ev-main{left:36px;top:2920px;width:501px;height:356px;background:linear-gradient(180deg,#3b3d41,#2a2c30)}
.ev-main .tags{position:absolute;left:36px;top:36px;color:#fff;font-size:13px}
.ev-main .heart{position:absolute;right:44px;top:20px;width:44px;height:38px;border:2px solid var(--blue);display:flex;align-items:center;justify-content:center}
.ev-main .date{position:absolute;left:36px;top:244px;color:#fff;font-size:14px}
.ev-main h4{position:absolute;left:36px;top:270px;color:#fff;font-size:18px;letter-spacing:.12em}
.ev-main .rm{position:absolute;left:36px;top:308px;color:var(--blue-link);font-weight:700;font-size:14px}
.ev{top:2920px;width:264px;height:356px;border:1px solid #ddd;box-shadow:0 2px 8px rgba(0,0,0,.12);background:#fff}
.ev .top{padding:30px 26px 22px;border-bottom:1px solid #ddd}
.ev em{color:var(--blue-link);font-size:13px}
.ev h4{font-size:17px;letter-spacing:.12em;margin:18px 0 24px}
.ev .date{font-size:14px;display:flex;align-items:center;gap:14px}
.cal{width:28px;height:26px;border:2px solid var(--blue);border-top-width:6px}
.ev .bot{padding:22px 26px;font-size:13px;line-height:1.7;color:var(--body);text-align:justify}
.ev .bot span{color:var(--blue-link);display:block;margin-top:16px}
/* footer */
.footer{left:0;top:3331px;width:1200px;height:331px;background:var(--footer);color:#fff}
.f-brand{left:34px;top:52px;display:flex;gap:14px;align-items:center;font-size:16px;font-weight:700;line-height:1.15;white-space:nowrap}
.f-brand i{width:34px;height:34px;border:3px solid #fff;border-radius:50%;flex:none}
.f-info{left:36px;top:147px;width:210px}
.f-about{font-size:13px;line-height:1.75;letter-spacing:.02em}
.socials{display:flex;gap:14px;margin-top:18px}
.socials i{width:22px;height:22px;border-radius:4px;background:var(--blue)}
.socials i:nth-child(3),.socials i:nth-child(4){background:#d33}
.fcol{top:34px;font-size:13px;line-height:2}
.fcol b{font-size:15px;display:block;margin-bottom:14px}
.field{border:1px solid #bbb;font-size:10px;padding:3px 8px;height:26px}
.subscribe{left:817px;top:206px;width:157px;height:26px;background:var(--blue);font-size:12px;font-weight:700;display:flex;align-items:center;justify-content:center}
.copy{left:0;top:298px;width:1200px;text-align:center;font-size:12px;font-weight:700}
</style>
</head>
<body>
<header>
  <div class="abs hero" role="img" aria-label="Photo of a shooter at an indoor range with wooden lane dividers"></div>
  <div class="abs topbar"></div>
  <div class="abs brand"><i></i><span>HALVERWOOD<br>MARKSMAN SPORTS</span></div>
  <div class="abs contact">Call us : +61-5550-418<span>Mail Id : hello@halverwood.example</span></div>
  <nav class="abs nav"><span class="on">Home</span><span>About us</span><span>Membership</span><span>Classes</span><span>Contact us</span><span>Cafe</span></nav>
  <div class="abs hero-box">
    <h1>STATE OF THE ART INDOOR<br>SHOOTING RANGE.</h1>
    <p>Lorem Ipsum is simply dummy text of the printing and typesetting industry. Lorem Ipsum has been the industry's standard dummy text ever since the 1500s.</p>
  </div>
  <div class="abs btn-read">Read More</div>
  <div class="abs btn-contact">Contact us</div>
</header>

<section>
  <h2 class="abs who-title"><span class="flag"></span>WHO WE ARE</h2>
  <div class="abs who-text">
    <p>With state-of-the-art indoor training facilities and full service custom shop on lion, we can accommodate most requests. All modern weapon enthussts can appreciate our broad services and real-world, experienced staff.</p>
    <p>Lorem Ipsum is simply dummy text of the printing and typesetting industry.Many desktop publishing packages and web page editors now use Lorem Ipsum as their default model text.</p>
    <p>All modern weaptons can appreciate our broad services and real-world, exper ienced taff.T fm nunc. Etiam pharetra, eratd fermentum feugiat, velit mauris aks egestasut</p>
    <p class="link" style="margin-top:30px">Read More</p>
  </div>
  <div class="abs tiles">
    <div class="tile"><svg class="edge" viewBox="0 0 363 97"><polygon points="1,1 320,1 362,96 43,96" fill="none" stroke="#cfcfcf"/></svg><div><b>Classes</b><small>Know More</small></div><svg class="ico" width="50" height="60" viewBox="0 0 50 60"><circle cx="30" cy="8" r="6" fill="#aaa"/><path d="M22 18h14l12-4v5l-12 5v12l6 18h-7l-5-14-8 14h-7l8-20z" fill="#aaa"/></svg></div>
    <div class="tile"><svg class="edge" viewBox="0 0 363 97"><polygon points="43,1 362,1 320,96 1,96" fill="none" stroke="#cfcfcf"/></svg><div><b>Shooting range</b><small>Know More</small></div><svg class="ico" width="64" height="64" viewBox="0 0 64 64" fill="none" stroke="#aaa" stroke-width="4"><circle cx="32" cy="32" r="22"/><circle cx="32" cy="32" r="10"/><path d="M32 2v16M32 46v16M2 32h16M46 32h16"/></svg></div>
    <div class="tile"><svg class="edge" viewBox="0 0 363 97"><polygon points="1,1 320,1 362,96 43,96" fill="none" stroke="#cfcfcf"/></svg><div><b>Membership</b><small>Know More</small></div><svg class="ico" width="66" height="44" viewBox="0 0 66 44" fill="#aaa"><circle cx="16" cy="12" r="8"/><circle cx="50" cy="12" r="8"/><circle cx="33" cy="14" r="10"/><path d="M0 40c0-12 8-18 16-18s10 4 10 4-6 6-6 14zM66 40c0-12-8-18-16-18s-10 4-10 4 6 6 6 14zM16 44c0-14 8-20 17-20s17 6 17 20z"/></svg></div>
  </div>
</section>

<section>
  <div class="abs range" role="img" aria-label="Dark textured backdrop with a close-up photo of a handgun"></div>
  <h2 class="abs range-title"><span class="flag"></span>HALVERWOOD MARKSMAN SPORTS</h2>
  <p class="abs range-text">Halverwood Marksman Sports will have 22 individual room lanes: 5 lanes at 25 yard range, 13 lanes at 10 yard ranges, and 4 lanes at 5 yard range dedicated to an advanced live fire interactive graphic experience.</p>
  <div class="abs card hours">
    <div class="card-head"><i></i>Our open hours will be</div>
    <div class="in">
      Monday – Thursday: 10am to 8pm<br>Friday &amp; Saturday: 9 am to 10pm<br><span class="red">Sunday: CLOSED</span>
      <p class="blue-b">First Wednesday of every month we will open at 6 am and close regularly.</p>
    </div>
  </div>
  <div class="abs card member">
    <div class="card-head"><i></i>Membership</div>
    <div class="in">
      <h3>Colorado’s Finest Indoor Shooting Range</h3>
      <p>We will also have a 22 foot wide open range for classes, corporate events, groups, and special training. There will be a 2,000 square foot retail area, small gunsmith corner, 2 classrooms that double as event rooms, dedicated range safety officer monitoring room, and small café.</p>
      <p class="more">More details</p>
    </div>
  </div>
</section>

<section>
  <h2 class="abs cafe-title"><span class="flag"></span>CAFE</h2>
  <p class="abs cafe-desc">Our Café will sell a small variety of coffee and mixed soda drinks. cinnamon rolls sold on a first come basis until sold out daily</p>
  <div class="abs food" style="left:88px"><div class="img" role="img" aria-label="Photo of a cup of coffee on a saucer" style="background:linear-gradient(160deg,#7a6a55,#b89a72 55%,#3b3028)"></div><div class="cap"><span>Variety of coffee</span><span>More items</span></div></div>
  <div class="abs food" style="left:453px"><div class="img" role="img" aria-label="Photo of a blue mixed soda drink with lime" style="background:linear-gradient(180deg,#f2f2f2,#e6eef2 40%,#bfe2ef 70%,#f2f2f2)"></div><div class="cap"><span>Mixed soda drinks</span><span>More items</span></div></div>
  <div class="abs food" style="left:819px"><div class="img" role="img" aria-label="Photo of iced cinnamon rolls" style="background:linear-gradient(170deg,#a8743f,#d2a26a 50%,#8a5a35)"></div><div class="cap"><span>Cinnamon rolls</span><span>More items</span></div></div>
</section>

<section>
  <div class="abs testi" role="img" aria-label="Dark backdrop with a photo of a bullet in motion"></div>
  <h2 class="abs testi-title"><span class="flag"></span>TESTMONIAL</h2>
  <div class="abs quote">“</div>
  <p class="abs testi-text">Neque porro quisquam est, qui dolorem ipsum quia dolor sit amet, consectetur, adipisci velit, sed quia non numquam eius modi tempora incidunt ut labore</p>
  <svg class="abs arrow" style="left:36px" viewBox="0 0 52 36"><path d="M30 8 20 18l10 10" fill="none" stroke="#fff" stroke-width="2"/></svg>
  <svg class="abs arrow" style="left:1112px" viewBox="0 0 52 36"><path d="M22 8l10 10-10 10" fill="none" stroke="#fff" stroke-width="2"/></svg>
</section>

<section>
  <h2 class="abs ev-title"><span class="flag"></span>UPCOMING EVENTS</h2>
  <div class="abs ev-main" role="img" aria-label="Photo of an instructor teaching a weapons class">
    <span class="tags">News, Weapons ,Training</span>
    <span class="heart"><svg width="22" height="20" viewBox="0 0 22 20"><path d="M11 19 2 10a5 5 0 0 1 9-6 5 5 0 0 1 9 6z" fill="#fff"/></svg></span>
    <span class="date">29-Sep-2019</span>
    <h4>WEAPON CLASSES - 2019</h4>
    <span class="rm">Read More</span>
  </div>
  <div class="abs ev" style="left:581px"><div class="top"><em>News,Guns</em><h4>WEAPON TRAINING</h4><div class="date"><i class="cal"></i>29-sep-2019</div></div><div class="bot">Lorem Ipsum is simply dummy text of the printing and typesetting industry.Many desktop publishing packages<span>Read More</span></div></div>
  <div class="abs ev" style="left:900px"><div class="top"><em>News,Guns</em><h4>WEAPON TRAINING</h4><div class="date"><i class="cal"></i>29-sep-2019</div></div><div class="bot">Lorem Ipsum is simply dummy text of the printing and typesetting industry.Many desktop publishing packages<span>Read More</span></div></div>
</section>

<footer class="abs footer">
  <div class="abs f-brand"><i></i><span>HALVERWOOD<br>MARKSMAN SPORTS</span></div>
  <div class="abs f-info">
    <p class="f-about">Lorem Ipsum is simply dummy text of the printing and typesetting industry.</p>
    <div class="socials"><i></i><i></i><i></i><i></i></div>
  </div>
  <div class="abs fcol" style="left:421px"><b>Quick link</b>Home<br>About us<br>Membership<br>Classes<br>Contact us</div>
  <div class="abs fcol" style="left:616px"><b>Company</b>Classes<br>Shooting<br>Membership<br>Cafe</div>
  <div class="abs fcol" style="left:817px"><b>Newsletters</b></div>
  <div class="abs field" style="left:817px;top:77px;width:161px">First name</div>
  <div class="abs field" style="left:1005px;top:77px;width:161px">Email id</div>
  <div class="abs field" style="left:817px;top:131px;width:349px;height:56px">Message</div>
  <div class="abs subscribe">SUBSCRIBE</div>
  <p class="abs copy">Copyright © 2019 Shooting Range.</p>
</footer>
</body>
</html>
```